Design of labels for exciting new natural skincare products...natural deodorant

I need some labels designed for a range of natural skincare, initially a natural deodorant paste. i will be offering a range of fragrances so i want a basic idea that i can drop different colours / ingredients into easily.

Fragrances are:
1. Jasmine, Orange and Bergamot
2. Lavender & Bergamot
3. Peppermint & Tea tree
4. Unscented
5. Lime, Lemongrass & Ginger

I am a new startup and will be selling online and through a couple of specialty online stores. The final design should encompass our ethos which is clean and green, not fussy nor clinical but friendly and easily accessible. I like fresh, contemporary modern look referencing vintage aesthetics.

The idea is that these products are better for your body AND the environment, and we pledge to use no plastic to package or distribute our products. i like the use of contemporary pastels such as soft pinks, tans and green/blue/aquas, though am open to new ideas too. the logo (attached) appears in red but that should not necessarily be used. i also like black and white with touches of colour.

Target Market(s)

Eco aware, health concious consumers with a reasonable skincare budget.

Industry/Entity Type

Skin Care Product

Font styles to use
Serif
Sans Serif
Decorative

Colors
2eb6a2
b768aa
eea4c8
fabb94
85cae6
cfeae6
eaf2ce
000000
eaeaea

Requirements
Must have
• Labels are for a small glass jar - the dimensions are 2cm high only and wrapping around the jar - at least 10cm wide. i'm also going to be providing a smaller size so this needs to be able to scale down to 1.5cm high and 8cm wide.
• the logo (supplied)
• title: Natural Deodorant
• Subtitle: Orange, Jasmine & Bergamot
• 45g
• Ingredients: tapioca starch*, bicarbonate of soda, Coconut oil*, shea butter*, mango butter*, diatomaceous earth*, sweet almond oil*, vitamin e*, tea tree oil*, Sweet orange essential oil*, Jasmine essential oil*, Bergamot essential oil*.
• *Certified organic ingredient
• (DESIGNERS - PLEASE NOTE NOT ALL THE INGREDIENTS ARE ORGANIC, PLEASE LIST THEM WITH A STAR * IF I HAVE SUPPLIED IT, THEN *Certified organic ingredient BELOW IN SLIGHTLY SMALLER TEXT - THIS SERVES AS THE KEY FOR THE INGREDIENTS LIST)
• wrenmeadow.nz
• Massage a pea-sized amount onto clean, dry armpits for an odour-free day.
• If irritation develops discontinue use and contact Wren Meadow. (please italicise the company name)
Nice to have
• open to ideas - i am attaching some examples of designs i like, you'll notice i swing between plain black and white aesthetics and a more decorative look. In general i like the old "medicine bottle" look, with hand sketched illustrations. But i'm open to ideas!

```html
<!DOCTYPE html>
<html lang="en">
<head>
<meta charset="utf-8">
<title>Wren Meadow – Natural Deodorant Label</title>
<link rel="stylesheet" href="https://fonts.googleapis.com/css2?family=Varela+Round&family=Oswald:wght@300&family=Roboto:ital,wght@0,400;1,400&display=swap">
<style>
  :root {
    --teal: #2eb6a2;
    --teal-deep: #31a896;
    --orchid: #b768aa;
    --label-grey: #dcdce0;
    --page: #f2f2f3;
    --ink: #1f1f1f;
    --ink-soft: #3a3a3a;
    --white: #ffffff;
    --citrus: #f2a93b;
    --leaf: #7faa4a;
    --badge-green: #3e8a4a;
  }
  * { margin: 0; padding: 0; box-sizing: border-box; }
  html, body { width: 1200px; height: 705px; overflow: hidden; }
  body {
    background: var(--page);
    font-family: "Roboto", Arial, sans-serif;
    color: var(--ink);
    position: relative;
  }
  .label {
    position: absolute;
    left: 0; top: 233px;
    width: 1200px; height: 238px;
    background: var(--label-grey);
    border-top: 7px solid var(--orchid);
    border-bottom: 7px solid var(--orchid);
  }
  .directions {
    position: absolute; left: 56px; top: 48px; width: 320px;
    letter-spacing: 0.08em;
  }
  .directions h2 { font-weight: 400; font-size: 17px; line-height: 20px; }
  .directions p { font-size: 15px; line-height: 18.5px; }
  .care-note {
    position: absolute; left: 56px; top: 132px; width: 320px;
    font-size: 11.5px; line-height: 15px; letter-spacing: 0.04em; color: var(--ink-soft);
  }
  .care-note em { font-style: italic; }
  .web-address {
    position: absolute; left: 56px; top: 172px;
    font-size: 13px; letter-spacing: 0.08em; color: var(--teal-deep);
  }
  .front-rule {
    position: absolute; left: 402px; top: 7px;
    width: 8px; height: 210px; background: var(--teal);
  }
  .brand {
    position: absolute; left: 466px; top: 22px; width: 244px;
    display: flex; align-items: center; justify-content: center; gap: 8px;
    font-family: "Varela Round", Arial, sans-serif;
    font-size: 24px; color: var(--teal);
  }
  .brand .dot { width: 10px; height: 10px; border-radius: 50%; background: var(--teal); }
  .title-ribbon { position: absolute; left: 434px; top: 76px; width: 308px; height: 30px; }
  .title-ribbon svg { position: absolute; inset: 0; }
  .title-ribbon h1 {
    position: relative; text-align: center; line-height: 30px;
    font-family: "Varela Round", Arial, sans-serif; font-weight: 400;
    font-size: 19px; color: var(--white); letter-spacing: 0.02em;
  }
  .fragrance {
    position: absolute; left: 434px; top: 109px; width: 308px;
    text-align: center; font-family: "Varela Round", Arial, sans-serif;
    font-size: 16px; letter-spacing: 0.03em;
  }
  .botanical {
    position: absolute; left: 456px; top: 140px; width: 92px; height: 62px;
    border-radius: 40% 50% 45% 40%;
    background: radial-gradient(circle at 40% 40%, var(--citrus), #f6d36a 45%, var(--leaf) 80%);
  }
  .vegan-mark {
    position: absolute; left: 630px; top: 150px; width: 58px; height: 34px;
    border-radius: 6px; background: var(--teal-deep); opacity: 0.85;
  }
  .net-weight {
    position: absolute; left: 558px; top: 196px; width: 60px;
    text-align: center; font-family: "Oswald", Arial, sans-serif; font-weight: 300;
    font-size: 17px; line-height: 22px; letter-spacing: 0.02em;
  }
  .ingredients { position: absolute; left: 874px; top: 28px; width: 300px; }
  .ingredients h3 {
    font-weight: 400; font-size: 15px; line-height: 18px;
    display: inline-block; border-bottom: 1px solid var(--ink);
  }
  .ingredients h3 + span { font-size: 15px; }
  .ingredients p { margin-top: 4px; font-size: 11.4px; line-height: 15.3px; }
  .ingredients .organic-key { margin-top: 2px; font-size: 10px; line-height: 13px; color: var(--ink-soft); }
  .cert-row {
    position: absolute; left: 874px; top: 162px;
    display: flex; align-items: center; gap: 10px;
  }
  .cert { flex: none; }
  .cert-circle { width: 52px; height: 52px; border-radius: 50%; border: 3px solid var(--badge-green); }
  .cert-square { width: 48px; height: 48px; border: 2px solid var(--ink); border-radius: 4px; }
  .cert-dot { width: 48px; height: 48px; border-radius: 50%; background: var(--badge-green); }
</style>
</head>
<body>
  <section class="label" aria-label="Natural deodorant jar label">
    <div class="directions">
      <h2>To use:</h2>
      <p>For an odour-free day,<br>massage a pea sized amount<br>onto clean, dry underarms.</p>
    </div>
    <p class="care-note">If irritation develops discontinue use<br>and contact <em>Wren Meadow</em>.</p>
    <p class="web-address">wrenmeadow.nz</p>

    <div class="front-rule"></div>

    <div class="brand"><span class="dot"></span>Wren Meadow</div>

    <div class="title-ribbon">
      <svg viewBox="0 0 308 30" width="308" height="30" preserveAspectRatio="none" aria-hidden="true">
        <polygon points="0,0 308,0 298,15 308,30 0,30 10,15" fill="var(--teal)"/>
      </svg>
      <h1>NATURAL DEODORANT</h1>
    </div>

    <p class="fragrance">Orange, Jasmine &amp; Bergamot</p>

    <div class="botanical" role="img" aria-label="Illustration of sliced oranges, bergamot and jasmine flowers with leaves"></div>

    <div class="vegan-mark" role="img" aria-label="Vegan certification badge"></div>

    <p class="net-weight">45g</p>

    <div class="ingredients">
      <h3>Ingredients</h3> <span>:</span>
      <p>Coconut oil*, tapioca starch*, bicarbonate of soda,<br>
      shea butter*, mango butter*, diatomaceous earth*,<br>
      sweet almond oil*, vitamin e*, tea tree oil*,<br>
      Sweet orange essential oil*, Jasmine essential oil*,<br>
      Bergamot essential oil*.</p>
      <p class="organic-key">*Certified organic ingredient</p>
    </div>

    <div class="cert-row">
      <div class="cert cert-circle" role="img" aria-label="Organic certification badge"></div>
      <div class="cert cert-square" role="img" aria-label="Cruelty-free badge"></div>
      <div class="cert cert-dot" role="img" aria-label="Recycling badge"></div>
      <svg class="cert" width="44" height="52" viewBox="0 0 44 52" role="img" aria-label="Period after opening symbol">
        <line x1="6" y1="20" x2="38" y2="4" stroke="var(--ink)" stroke-width="2"/>
        <path d="M4 28 H40 V46 Q22 52 4 46 Z" fill="var(--white)" stroke="var(--ink)" stroke-width="1.5"/>
      </svg>
    </div>
  </section>
</body>
</html>
```